IT Professional business card with a hometown feel and a little edgy.

My business name is Tamble Website Solutions. But I have ended up doing much more. I live in a very small remote community, where everyone knows everyone. We like the one-on-one customer service in this community. I do computer tutoring, virus removal, networking, and software training. My clients are businesses and private individuals.

My website is tamblewebsitesolutions.example, when I first designed it I was going for a fresh, clean look, which I still like. But I am thinking about making the website a bit more edgy to match my new logo from ArtHively (logo attached). At this time my website does not display the new logo, but I plan on redesigning the website in the future to match the logo and business card.

My tag line is "let the internet work for you"

I'm thinking I would like to have the business card printed with a metallic finish.
Updates

Please do not use black backgrounds, or any solid dark colors. Prefer light or white backgrounds.

Target Market(s)

Small businesses. Individuals that need computer help at home.

Industry/Entity Type

It Company

Contact Information for Business Card

Nora Prandell
Tamble Website Solutions
PO Box 7153
Alderwick, WA 98765
Cell: 555-271-3096
nora@tamblewebsitesolutions.example
tamblewebsitesolutions.example

Font styles to use
Serif

Requirements
Must have
• Must have all the information listed in "Business Card Details"
• Must use the logo provided.
• Use the colors from the provided logo
Nice to have
• Would like to use my tagline "let the internet work for you" all lowercase

```html
<!DOCTYPE html>
<html lang="en">
<head>
<meta charset="utf-8">
<title>Tamble Website Solutions — Business Card</title>
<link rel="stylesheet" href="https://fonts.googleapis.com/css2?family=Noto+Serif:wght@400;700&family=Open+Sans:wght@400;600&display=swap">
<style>
  :root {
    --page-bg: #eceee9;
    --green-dark: #3f8a3c;
    --green-mid: #5ba653;
    --green-light: #9fcf84;
    --paper: #ffffff;
    --paper-shade: #e6e6e6;
    --divider-grey: #4b4b4d;
    --ink-light: #ffffff;
    --brand-green: #3f9a3a;
  }
  * { box-sizing: border-box; margin: 0; padding: 0; }
  html, body { width: 1200px; height: 780px; overflow: hidden; }
  body {
    background: var(--page-bg);
    display: flex;
    align-items: center;
    justify-content: center;
    gap: 40px;
    font-family: "Noto Serif", Georgia, serif;
  }
  .card {
    position: relative;
    width: 540px;
    height: 309px;
    border-radius: 4px;
    overflow: hidden;
    box-shadow: 0 10px 28px rgba(0,0,0,.18);
  }

  /* Front */
  .card-front { background: radial-gradient(ellipse at 62% 60%, var(--green-light) 0%, var(--green-mid) 45%, var(--green-dark) 100%); }
  .front-split { position: absolute; inset: 0; width: 100%; height: 100%; }
  .front-brand {
    position: absolute;
    left: 34px; top: 122px;
    display: flex; align-items: center; gap: 12px;
  }
  .brand-square { width: 26px; height: 26px; background: var(--brand-green); flex: none; }
  .brand-name {
    font-family: "Noto Serif", Georgia, serif;
    font-weight: 700;
    font-size: 19px;
    line-height: 1.2;
    color: var(--brand-green);
    width: 150px;
  }
  .front-details {
    position: absolute;
    right: 26px; top: 24px; bottom: 22px;
    width: 300px;
    color: var(--ink-light);
    text-align: right;
    display: flex; flex-direction: column;
  }
  .company { font-size: 19px; font-weight: 700; letter-spacing: .2px; }
  .person { font-size: 16px; margin-top: 22px; }
  .address { font-size: 12px; line-height: 1.5; margin-top: 8px; }
  .contact { margin-top: auto; font-size: 11.5px; line-height: 1.7; }
  .contact-line { display: flex; justify-content: flex-end; align-items: center; gap: 6px; }
  .contact-icon { width: 13px; height: 13px; flex: none; }

  /* Back */
  .card-back {
    background: radial-gradient(ellipse at 45% 40%, var(--green-light) 0%, var(--green-mid) 45%, var(--green-dark) 100%);
    color: var(--ink-light);
  }
  .back-lockup {
    position: absolute;
    left: 110px; top: 92px;
    display: flex; align-items: center; gap: 20px;
  }
  .back-mark {
    display: flex; align-items: center; gap: 12px;
  }
  .back-mark .brand-square { background: var(--ink-light); width: 34px; height: 34px; }
  .back-mark .brand-name { color: var(--ink-light); font-size: 22px; width: 170px; }
  .back-rule { width: 1.5px; height: 96px; background: var(--ink-light); }
  .back-tag {
    font-family: "Open Sans", Arial, sans-serif;
    font-size: 17px; line-height: 1.15;
  }
  .back-web {
    position: absolute;
    left: 0; right: 0; bottom: 30px;
    text-align: center;
    font-size: 13px;
    letter-spacing: .3px;
  }
</style>
</head>
<body>

  <section class="card card-front" aria-label="Business card front">
    <svg class="front-split" viewBox="0 0 540 309" preserveAspectRatio="none" aria-hidden="true">
      <defs>
        <linearGradient id="paperShade" x1="0" y1="0" x2="1" y2="1">
          <stop offset="0" stop-color="#ffffff"/>
          <stop offset="1" stop-color="#e4e4e4"/>
        </linearGradient>
      </defs>
      <path d="M0 0 H150 C200 70 250 140 232 309 H0 Z" fill="#4b4b4d"/>
      <path d="M0 0 H140 C188 70 236 140 218 309 H0 Z" fill="url(#paperShade)"/>
    </svg>

    <div class="front-brand">
      <span class="brand-square"></span>
      <span class="brand-name">Tamble Website Solutions</span>
    </div>

    <div class="front-details">
      <p class="company">Tamble Website Solutions</p>
      <p class="person">Nora Prandell</p>
      <p class="address">PO Box 7153<br>Alderwick, WA 98765</p>
      <div class="contact">
        <p class="contact-line">555-271-3096
          <svg class="contact-icon" viewBox="0 0 16 16" aria-label="phone"><rect x="0" y="0" width="16" height="16" fill="#fff"/><path d="M4 3l2 0 1 3-1.5 1a7 7 0 0 0 3.5 3.5L10 9l3 1v2c0 1-1 1-1 1A9 9 0 0 1 3 4s0-1 1-1z" fill="#3f8a3c"/></svg>
        </p>
        <p class="contact-line">nora@tamblewebsitesolutions.example
          <svg class="contact-icon" viewBox="0 0 16 16" aria-label="email"><rect x="0" y="0" width="16" height="16" fill="#fff"/><rect x="3" y="4.5" width="10" height="7" fill="none" stroke="#3f8a3c" stroke-width="1.3"/><path d="M3 4.5l5 4 5-4" fill="none" stroke="#3f8a3c" stroke-width="1.3"/></svg>
        </p>
        <p class="contact-line">www.tamblewebsitesolutions.example</p>
      </div>
    </div>
  </section>

  <section class="card card-back" aria-label="Business card back">
    <div class="back-lockup">
      <div class="back-mark">
        <span class="brand-square"></span>
        <span class="brand-name">Tamble</span>
      </div>
      <span class="back-rule"></span>
      <p class="back-tag">Tamble<br>Website<br>Solutions</p>
    </div>
    <p class="back-web">www.tamblewebsitesolutions.example</p>
  </section>

</body>
</html>
```